Modern and Improved business card design for Family Dental Practice

We have 2 sets of logo we have designed and now just need a business card layout and design for the office. Colors are on the logo. We can choose which logo we want to go with . The font can be changed to whatever seems modern and relevant. We are family dental office that has been open for over 15 years in South Austin Texas.

Target Market(s)

Handout Business cards to referrals and specialists

Industry/Entity Type

Dental

Contact Information for Business Card

We need address, phone, website and email address. 4870 North Loop Rd Suite 208 , Austin,Texas 78651....phone: 512-480-7319.....email- info@maplebrookdental-example.com....website - MapleBrookDental-example.com

Font styles to use
Serif
Decorative

Requirements
Must have
• my logo. We have 2 logos, but we can use just one or if we can incorporate one on one side and the other on the other side.
Nice to have
• Really just need a modern look and clean that incorporates the logo and colors .

```html
<!DOCTYPE html>
<html lang="en">
<head>
<meta charset="utf-8">
<title>Maple Brook Family Dentistry – Business Card</title>
<link rel="stylesheet" href="https://fonts.googleapis.com/css2?family=Montserrat:wght@400;500;600;700&display=swap">
<style>
  :root {
    --page-bg: #e9e6e1;
    --card-white: #ffffff;
    --brand-green: #1f8a3c;
    --title-green: #4a8f2e;
    --olive-light: #f4f6ef;
    --olive-deep: #a7b866;
    --text-dark: #333333;
    --text-grey: #555555;
    --rule: #6b6b5a;
    --box-green: #4f9a45;
  }
  * { margin: 0; padding: 0; box-sizing: border-box; }
  html, body { width: 900px; height: 1200px; overflow: hidden; }
  body {
    background: var(--page-bg);
    font-family: "Montserrat", Arial, sans-serif;
    color: var(--text-dark);
    position: relative;
  }
  .card {
    position: absolute;
    left: 80px;
    width: 742px;
    height: 440px;
    border-radius: 40px;
    overflow: hidden;
  }
  .card-front { top: 132px; background: var(--card-white); }
  .card-back {
    top: 638px;
    background: linear-gradient(to bottom, var(--olive-light) 0%, #ffffff 22%, #dfe6c8 50%, var(--olive-deep) 100%);
  }

  /* Front */
  .brand {
    position: absolute;
    left: 66px;
    top: 180px;
    display: flex;
    align-items: center;
    gap: 14px;
  }
  .brand-dot {
    width: 22px; height: 22px; border-radius: 50%;
    background: var(--brand-green);
    flex: none;
  }
  .brand-name {
    font-size: 24px;
    font-weight: 500;
    color: var(--brand-green);
    letter-spacing: 1px;
    text-transform: uppercase;
    line-height: 1.2;
    white-space: nowrap;
  }
  .divider {
    position: absolute;
    left: 384px; top: 132px;
    width: 2px; height: 195px;
    background: var(--brand-green);
  }
  .person { position: absolute; left: 418px; top: 124px; white-space: nowrap; }
  .person-name { font-size: 25px; font-weight: 700; color: var(--brand-green); }
  .person-role { font-size: 16px; color: var(--text-grey); margin-top: 4px; }
  .address {
    position: absolute; left: 415px; top: 200px;
    font-size: 16px; line-height: 20px; color: var(--text-dark);
    white-space: nowrap;
  }
  .contacts { position: absolute; left: 416px; top: 264px; list-style: none; }
  .contacts li {
    display: flex; align-items: center; gap: 7px;
    font-size: 14.5px; height: 23px; color: var(--text-dark);
    white-space: nowrap;
  }
  .contacts li.phone { font-size: 16.5px; margin-bottom: 2px; }
  .contacts svg { width: 13px; height: 13px; flex: none; fill: var(--brand-green); }

  /* Back */
  .appt-title {
    position: absolute; left: 0; right: 0; top: 74px;
    text-align: center;
    font-size: 31px; font-weight: 700; color: var(--title-green);
  }
  .field { position: absolute; left: 34px; right: 36px; display: flex; align-items: flex-end; font-size: 16px; color: var(--text-grey); }
  .field span:first-child { width: 66px; flex: none; }
  .field .line { flex: 1; border-bottom: 1px solid var(--rule); height: 1px; margin-bottom: 6px; }
  .field-name { top: 146px; }
  .field-date { top: 186px; }
  .field-note { top: 326px; left: 37px; }
  .note-extra { position: absolute; left: 36px; right: 36px; top: 383px; border-bottom: 1px solid var(--rule); }
  .days {
    position: absolute; left: 34px; right: 36px; top: 265px;
    display: flex; justify-content: space-between; list-style: none;
    font-size: 16px; color: var(--text-grey);
  }
  .days li { display: flex; align-items: center; gap: 9px; }
  .days .box { width: 20px; height: 20px; border: 1.5px solid var(--box-green); }
</style>
</head>
<body>
  <section class="card card-front">
    <div class="brand">
      <span class="brand-dot"></span>
      <span class="brand-name">Maple Brook<br>Family Dentistry</span>
    </div>
    <div class="divider"></div>
    <div class="person">
      <h1 class="person-name">Dr. Daniel R Moore</h1>
      <p class="person-role">Owner</p>
    </div>
    <p class="address">4870 North Loop Rd Suite 208<br>Austin,Texas 78651</p>
    <ul class="contacts">
      <li class="phone">
        <svg viewBox="0 0 16 16" aria-hidden="true"><path d="M2 6c0-2 3-3 6-3s6 1 6 3v1h-3V5.5C10 5 9 5 8 5s-2 0-3 .5V7H2z M4 8h8l1.5 6h-11z"/></svg>
        512-480-7319
      </li>
      <li>
        <svg viewBox="0 0 16 16" aria-hidden="true"><path d="M1 3h14v1.5L8 9 1 4.5z M1 6l7 4.5L15 6v7H1z"/></svg>
        info@maplebrookdental-example.com
      </li>
      <li>
        <svg viewBox="0 0 16 16" aria-hidden="true"><circle cx="8" cy="8" r="7"/><path d="M5 4c2 1 1 3 3 3s1 3 3 3" stroke="#fff" stroke-width="1.3" fill="none"/></svg>
        www.MapleBrookDental-example.com
      </li>
    </ul>
  </section>

  <section class="card card-back">
    <h2 class="appt-title">Next Appoinment</h2>
    <div class="field field-name"><span>Name</span><span class="line"></span></div>
    <div class="field field-date"><span>Date</span><span class="line"></span></div>
    <ul class="days">
      <li>Sun <span class="box"></span></li>
      <li>Mon <span class="box"></span></li>
      <li>Tue <span class="box"></span></li>
      <li>Wed <span class="box"></span></li>
      <li>Thu <span class="box"></span></li>
      <li>Fri <span class="box"></span></li>
      <li>Sat <span class="box"></span></li>
    </ul>
    <div class="field field-note"><span>Note</span><span class="line"></span></div>
    <div class="note-extra"></div>
  </section>
</body>
</html>
```